GLP letterhead

We need a letterhead design for our new company based in Los Angeles called "Gold Lantern Pictures". We develop film and television projects. We work with investors, financiers, film production companies, film distribution and sales companies as well as studios. We would like to incorporate our logo (see attached) but make the letterhead simple and elegant. We need to include: logo, company address, phone number and company website.
Updates

Hello designers, Thanks for your submissions. For our letterhead, we are looking for something more simple and elegant. No heavy bars or lines. Make it feel light and clean. Not a lot of ink on the page. Use the logo and contact info but think "clean", "streamlined" and mostly white paper. Looking forward to seeing more... thanks! Gold Lantern Pictures team

Target Market(s)

Studio executives, talent agents and agencies, financiers, investors.

Industry/Entity Type

It Company

Requirements
Must have
• Gold Lantern Pictures logo (see attached). Logo may be cropped and altered appropriately for elegant letterhead design.
• Please include:
• COMPANY ADDRESS:
• Ridgeway Studio Park
• 2850 Halverson Street
• Tower Annex, 6th Floor
• Harbor Point, CA 90412
• COMPANY WEBSITE:
• www.goldlanternpicturesco.example
• COMPANY PHONE NUMBER:
• 310-555-0148

```html
<!DOCTYPE html>
<html lang="en">
<head>
<meta charset="utf-8">
<title>Gold Lantern Pictures — Letterhead</title>
<link rel="stylesheet" href="https://fonts.googleapis.com/css2?family=Montserrat:wght@400;500;600&display=swap">
<style>
  :root {
    --backdrop: #e6eaec;
    --paper: #ffffff;
    --ink: #1c1c1c;
    --ink-soft: #3a3d40;
    --accent: #1a9fd3;
    --mark-dark: #0d0f12;
    --emboss: #eeeeee;
  }
  html, body {
    margin: 0;
    padding: 0;
    width: 1200px;
    height: 1000px;
    overflow: hidden;
    background: var(--backdrop);
    font-family: "Montserrat", Arial, sans-serif;
  }
  .letterhead {
    position: absolute;
    left: 271px;
    top: 30px;
    width: 658px;
    height: 940px;
    background: var(--paper);
    box-shadow: 0 2px 10px rgba(0,0,0,0.08);
  }
  .brand {
    position: absolute;
    left: 104px;
    top: 67px;
    display: flex;
    flex-direction: column;
    align-items: center;
    gap: 10px;
    width: 134px;
  }
  .brand-disc {
    width: 68px;
    height: 68px;
    border-radius: 50%;
    background: var(--mark-dark);
    border: 3px solid var(--accent);
    box-sizing: border-box;
  }
  .brand-name {
    margin: 0;
    font-size: 12px;
    font-weight: 600;
    letter-spacing: 0.08em;
    text-transform: uppercase;
    text-align: center;
    line-height: 1.3;
    color: var(--ink);
  }
  .contact {
    position: absolute;
    left: 443px;
    top: 145px;
    margin: 0;
    font-style: normal;
    font-size: 7.5px;
    font-weight: 400;
    line-height: 1.45;
    color: var(--ink-soft);
    white-space: nowrap;
  }
  .contact span { display: block; }
  .watermark {
    position: absolute;
    left: 104px;
    top: 314px;
    width: 454px;
    height: 454px;
  }
</style>
</head>
<body>
  <main class="letterhead">
    <header class="brand">
      <div class="brand-disc"></div>
      <p class="brand-name">Gold Lantern Pictures</p>
    </header>

    <address class="contact">
      <span>Office: Ridgeway Studio Park 2850 Halverson</span>
      <span>Street Tower Annex, 6th Floor</span>
      <span>Harbor Point, CA 90412</span>
      <span>Tel: 310-555-0148</span>
      <span>Web: www.goldlanternpicturesco.example</span>
    </address>

    <svg class="watermark" viewBox="0 0 454 454" aria-hidden="true">
      <circle cx="227" cy="227" r="225" fill="none" stroke="var(--emboss)" stroke-width="3"/>
    </svg>
  </main>
</body>
</html>
```